KV Taxidermy

I need business Cards with my logo and a background photo of one of my taxidermy mounts.
I would like a black back drop behind it all and what ever looks best for my contact information (red or white?)
Marcus Pellow
555-218-4907
kvtaxidermy512@mailvex.net
Chatterly page

```html
<!DOCTYPE html>
<html lang="en">
<head>
<meta charset="utf-8">
<title>KV Taxidermy – Business Cards</title>
<link href="https://fonts.googleapis.com/css2?family=Roboto:wght@300;400;700;900&display=swap" rel="stylesheet">
<style>
  :root {
    --page-bg: #f2f2f2;
    --card-bg: #231f20;
    --ink-white: #ffffff;
    --ink-grey: #8a8a8a;
    --mark-faint: #333031;
    --mount-light: #e9e7e2;
    --mount-mid: #b9b6b0;
    --rock: #5f6670;
  }
  html, body {
    margin: 0;
    width: 1200px;
    height: 1200px;
    overflow: hidden;
    background: var(--page-bg);
    font-family: "Roboto", sans-serif;
  }
  .canvas {
    position: relative;
    width: 1200px;
    height: 1200px;
  }
  .card {
    position: absolute;
    left: 150px;
    width: 900px;
    height: 514px;
    background: var(--card-bg);
    overflow: hidden;
    box-shadow: 0 6px 18px rgba(0,0,0,0.18);
  }
  .card--front { top: 60px; }
  .card--back { top: 626px; }

  /* Front */
  .brand-faint {
    position: absolute;
    top: 44px;
    left: 500px;
    display: flex;
    align-items: center;
    gap: 10px;
    color: var(--mark-faint);
    font-weight: 700;
    font-size: 22px;
    letter-spacing: 2px;
  }
  .brand-faint .brand-square {
    width: 18px; height: 18px; background: var(--mark-faint);
  }
  .mount-photo {
    position: absolute;
    left: 100px;
    top: 150px;
    width: 660px;
    height: 320px;
    border-radius: 40% 50% 20% 30% / 50% 50% 30% 40%;
    background: linear-gradient(160deg, var(--mount-light) 0%, var(--mount-mid) 55%, var(--rock) 100%);
  }

  /* Back */
  .brand {
    position: absolute;
    top: 90px;
    left: 0;
    right: 0;
    display: flex;
    justify-content: center;
    align-items: center;
    gap: 14px;
    color: var(--ink-white);
    font-weight: 700;
    font-size: 36px;
    letter-spacing: 3px;
  }
  .brand .brand-square {
    width: 30px; height: 30px; background: var(--ink-white);
  }
  .person {
    position: absolute;
    top: 205px;
    left: 280px;
    color: var(--ink-white);
  }
  .person-name {
    font-weight: 900;
    font-size: 42px;
    line-height: 1;
  }
  .person-role {
    margin-top: 8px;
    font-weight: 300;
    font-size: 28px;
  }
  .tab {
    position: absolute;
    width: 96px;
    height: 58px;
    background: var(--ink-white);
    display: flex;
    align-items: center;
    justify-content: center;
  }
  .tab--email { right: 0; top: 190px; border-radius: 29px 0 0 29px; }
  .tab--phone { left: 0; bottom: 70px; border-radius: 0 29px 29px 0; }
  .email {
    position: absolute;
    right: 40px;
    top: 300px;
    color: var(--ink-white);
    font-weight: 700;
    font-size: 28px;
  }
  .phone {
    position: absolute;
    left: 120px;
    bottom: 80px;
    color: var(--ink-white);
    font-weight: 700;
    font-size: 32px;
  }
  .get-in-touch {
    position: absolute;
    left: 420px;
    bottom: 84px;
    display: flex;
    align-items: center;
    gap: 22px;
    font-weight: 700;
    font-size: 22px;
  }
  .get-in-touch-label { color: var(--ink-grey); }
  .social {
    display: flex;
    align-items: center;
    gap: 8px;
    color: var(--ink-white);
    font-weight: 400;
  }
  .social-dot {
    width: 18px; height: 18px; border-radius: 50%;
    border: 2px solid var(--ink-white);
  }
</style>
</head>
<body>
<div class="canvas">

  <section class="card card--front">
    <div class="brand-faint"><span class="brand-square"></span>KV TAXIDERMY</div>
    <div class="mount-photo" role="img" aria-label="Photo of a white Dall sheep ram taxidermy mount resting on a grey rock base"></div>
  </section>

  <section class="card card--back">
    <div class="brand"><span class="brand-square"></span>KV TAXIDERMY</div>

    <div class="person">
      <div class="person-name">Marcus Pellow</div>
      <div class="person-role">Position Here</div>
    </div>

    <div class="tab tab--email">
      <svg width="26" height="20" viewBox="0 0 26 20" aria-hidden="true">
        <rect x="1.5" y="1.5" width="23" height="17" rx="2" fill="none" stroke="#231f20" stroke-width="2"/>
        <path d="M2 3 L13 11 L24 3" fill="none" stroke="#231f20" stroke-width="2"/>
      </svg>
    </div>
    <div class="email">kvtaxidermy512@mailvex.net</div>

    <div class="get-in-touch">
      <span class="get-in-touch-label">GET IN TOUCH</span>
      <span class="social"><span class="social-dot"></span>Chatterly · KV TAXIDERMY</span>
    </div>

    <div class="tab tab--phone">
      <svg width="20" height="32" viewBox="0 0 20 32" aria-hidden="true">
        <rect x="1.5" y="1.5" width="17" height="29" rx="3" fill="none" stroke="#231f20" stroke-width="2"/>
        <line x1="7" y1="26" x2="13" y2="26" stroke="#231f20" stroke-width="2"/>
      </svg>
    </div>
    <div class="phone">555-218-4907</div>
  </section>

</div>
</body>
</html>
```